Ebook cover needed for my Pagelit Crime Novel

My ebook takes place on a fictional island off the coast of Sydney, Australia. A 10 year old German boy, holidaying with his family, is found drowned just minutes after playing happily on a rope swing on a sunny day at Wren Creek. But an investigative journalist - and the boy's parents - think the police got it wrong. Is there a killer on the island? The cover must be bold, simple and the graphic image and print suitable for clear thumbprint viewing on Brightmart. The title is CHILD OF WREN CREEK and the author is MARGOT HASKELL. I'm looking for a stand-out cover that is designed to catch the reader's eye and is easy to read. I don't want a picture of a boy and would prefer something more abstract than literal.

Target Market(s)

Crime and thriller readers, women and men, all ages (adult)

Font styles to use
Serif
Sans Serif

Requirements
Must have
• A bold design, be evocative of murder without being too obvious (eg there is no blood or weapons because the boy drowns). The title needs to be around a third of the cover and my name should be as wide as the cover.
Nice to have
• These things are just thoughts, please don't feel you need to constrain your design ideas.
• A boy's hand on a tree. Some torn refill paper with handwriting in pen. A rope swing hanging from a tree. A river shot (narrow river not wide). Wilted flowers at the base of a tree. A finch (Australian bird) the river is named after - not necessarily a photo but a silhouette perhaps? A sense of the title being under water. A a blond boy's head from behind (just his hair).
Should not have
• A boy's face. Anything relating to a dark or stormy day or night - he disappears on a sunny day.

```html
<!DOCTYPE html>
<html lang="en">
<head>
<meta charset="utf-8">
<title>Child of Wren Creek — Margot Haskell</title>
<link rel="stylesheet" href="https://fonts.googleapis.com/css2?family=Uncial+Antiqua&display=swap">
<style>
  :root {
    --amber-core: #f2b13a;
    --amber-mid: #e0801f;
    --rust-edge: #b8361a;
    --ember-edge: #8e1f12;
    --frame-brown: #4a2510;
    --frame-dark: #2a1207;
    --frame-gold: #d8a84a;
    --type-fill: #fbf3e6;
    --type-outline: #2b1608;
    --meadow: #6f9a3a;
    --meadow-deep: #2f4a1c;
    --shadow-band: #15180f;
    --creek-blue: #2a4f86;
    --creek-light: #dfe8f2;
  }
  html, body {
    margin: 0;
    padding: 0;
    width: 841px;
    height: 1200px;
    overflow: hidden;
    background: #ffffff;
  }
  .cover {
    position: relative;
    width: 841px;
    height: 1200px;
    overflow: hidden;
    background:
      radial-gradient(ellipse 62% 52% at 50% 46%, var(--amber-core) 0%, var(--amber-mid) 48%, var(--rust-edge) 82%, var(--ember-edge) 100%);
  }
  .cover__art {
    position: absolute;
    inset: 0;
    width: 841px;
    height: 1200px;
  }
  .cover__title,
  .cover__author {
    position: absolute;
    left: 0;
    right: 0;
    margin: 0;
    text-align: center;
    font-family: "Uncial Antiqua", serif;
    font-weight: 400;
    color: var(--type-fill);
    text-transform: uppercase;
    -webkit-text-stroke: 2px var(--type-outline);
    text-shadow: 3px 3px 0 var(--type-outline), 0 0 10px rgba(43, 22, 8, 0.6);
    line-height: 1;
  }
  .cover__title {
    top: 58px;
    font-size: 74px;
    letter-spacing: 1px;
  }
  .cover__title span,
  .cover__author span { display: block; }
  .cover__title span + span { margin-top: 8px; }
  .cover__author {
    top: 962px;
    font-size: 80px;
    letter-spacing: 2px;
  }
  .cover__author span + span { margin-top: 6px; }
</style>
</head>
<body>
  <main class="cover">
    <svg class="cover__art" viewBox="0 0 841 1200" xmlns="http://www.w3.org/2000/svg">
      <defs>
        <linearGradient id="frameRing" x1="0" y1="0" x2="1" y2="1">
          <stop offset="0" stop-color="var(--frame-brown)"/>
          <stop offset="0.5" stop-color="var(--frame-dark)"/>
          <stop offset="1" stop-color="var(--frame-brown)"/>
        </linearGradient>
        <linearGradient id="creekScene" x1="0" y1="0" x2="0" y2="1">
          <stop offset="0" stop-color="var(--shadow-band)"/>
          <stop offset="0.12" stop-color="var(--meadow-deep)"/>
          <stop offset="0.3" stop-color="var(--meadow)"/>
          <stop offset="0.45" stop-color="var(--meadow-deep)"/>
          <stop offset="0.6" stop-color="var(--shadow-band)"/>
          <stop offset="0.75" stop-color="var(--creek-light)"/>
          <stop offset="0.88" stop-color="var(--creek-blue)"/>
          <stop offset="1" stop-color="var(--meadow-deep)"/>
        </linearGradient>
        <clipPath id="ovalWindow">
          <ellipse cx="422" cy="690" rx="165" ry="405"/>
        </clipPath>
      </defs>
      <g class="oval-frame">
        <ellipse cx="428" cy="698" rx="200" ry="442" fill="rgba(40,12,4,0.45)"/>
        <ellipse cx="422" cy="690" rx="196" ry="438" fill="url(#frameRing)"/>
        <ellipse cx="422" cy="690" rx="194" ry="436" fill="none" stroke="var(--frame-gold)" stroke-width="2"/>
        <ellipse cx="422" cy="690" rx="169" ry="409" fill="none" stroke="var(--frame-gold)" stroke-width="3"/>
      </g>
      <rect class="oval-frame__scene" x="257" y="285" width="330" height="810"
            fill="url(#creekScene)" clip-path="url(#ovalWindow)"
            role="img" aria-label="Photograph of a grassy creek bank with sunlit reeds reflected in the narrow creek water"/>
    </svg>

    <h1 class="cover__title">
      <span>Child of</span>
      <span>Wren Creek</span>
    </h1>

    <p class="cover__author">
      <span>Margot</span>
      <span>Haskell</span>
    </p>
  </main>
</body>
</html>
```